Flyer-Design für ein Baumhaushotel
Zielgruppe
Baumhaushotel. Hochwertige und gehobene Ausstattung. Fokus Natur und Ruhe.
Naturliebhaber, Großstadtmensch der eine Auszeit sucht
Aufgabenstellung
Flyer dreichfach gefaltet, beidseitig bedruckt
Fotos haben wir hochgeladen, eine höhere Auflösung ist auch vorhanden.
Texte können auch gern von unserer Website genommen werden: waldnest-kojen.de
Nicht zu viel Text, z.B. diesen Text:
evtl einfach nur Stichwörter locker einfügen wie zB (dies ist nur eine Auswahl)
zwischen den Bäumen träumen
in vier Metern Höhe
barrierefreies Baumhaus mit vielen Features
Kaminofen
Bad mit Dusche & WC
Pantry-Küche
gemütlich
Echtholzfußboden
atemberaubende Ausblicke, hoher Komfort und Natur pur.
an einem Seengebiet in der Nähe des Deiches, hinter dem die Elbe in die Nordsee mündet.
eine besondere Auszeit hoch über dem Erdboden
Wenn vom Design sinnvoll, kann man noch Vorteile einbringen wie zB etwas von dieser Auflistung (muss aber auch nicht genannt werden)
! auf jeden Fall soll unser barrierefreies Kiebitz-Baumhaus genannt und gezeigt werden !
30qm Baumhäuser in vier Meter Höhe inkl. Bad und Pantry-Küche, Schlafbereich, Couchecke und Essbereich
10qm Außenterrasse auf 2,50m Höhe inkl. Strandkorb
einzigartiges großes barrierefreies Baumhaus (57qm) , mit barrierefreiem Bad und vielen Features sowie Fußbodenerwärmung, dieses Haus ist für bis zu 6 Personen nutzbar, alle anderen Baumhäuser bis zu 4 Personen
Wlan, TV, Heizung, Kaminofen und voll ausgestattete Küche
Parkplatz direkt im Einfahrtbereich inklusive – das Baumhaushotel-Gelände selbst ist autofrei
haustierfreie und haustierfreundliche Baumhäuser verfügbar
Bettwäsche, Handtücher und Kaminholz inklusive
hoteleigene Kanus und Bootsanleger am Drei-Seengebiet inklusive
von alten Bäumen umgebendes Baumhausgelände inkl. Waldbad (im Sinne von Shinrin Yoku)
Baumhaushotel liegt direkt neben Drei-Seengebiet und in Deichnähe zur Elbe/ Nordsee
spezieller Rückzugsbereich für Tiere, den wir Menschen nicht betreten – Tierbeo..

```html
<!DOCTYPE html>
<html lang="de">
<head>
<meta charset="utf-8">
<title>waldnest-kojen.de – Flyer</title>
<link rel="stylesheet" href="https://fonts.googleapis.com/css2?family=Josefin+Sans:wght@400;600&family=Kaushan+Script&display=swap">
<style>
  :root {
    --bark: #6f4a3a;
    --ink: #141010;
    --leaf: #3f6b45;
    --paper: #ffffff;
    --roof: #3b3a3a;
    --wood-light: #c9925c;
    --wood-mid: #b07a4a;
    --rail: #a9a8a2;
    --grass: #6e7a52;
    --ceiling: #ece6df;
    --ceiling-wood: #c58a52;
    --wall: #d9cfc6;
    --linen: #b9b5b2;
  }
  * { margin: 0; padding: 0; box-sizing: border-box; }
  html, body {
    width: 1200px; height: 834px; overflow: hidden;
    background: var(--paper);
  }
  .flyer { position: relative; width: 1200px; height: 834px; }
  .panel {
    position: absolute; top: 2px; height: 830px;
    background: var(--bark); overflow: hidden;
  }
  .panel--cover { left: 0; width: 587px; }
  .panel--info { left: 610px; width: 590px; }
  .photo { position: absolute; inset: 0; width: 100%; height: 100%; }
  .brand {
    position: absolute;
    font-family: "Kaushan Script", cursive;
    color: var(--ink);
    white-space: nowrap;
    line-height: 1;
  }
  .panel--cover .brand { left: 228px; top: 246px; font-size: 46px; }
  .panel--info .brand { left: 264px; top: 424px; font-size: 39px; }
  .features {
    position: absolute;
    font-family: "Josefin Sans", sans-serif;
    color: var(--ink);
    font-size: 15px;
    line-height: 25.5px;
  }
  .features h2 { font-size: 17px; font-weight: 600; margin-bottom: 2px; line-height: 24px; }
  .features ul { list-style: none; position: relative; z-index: 0; }
  .features li { position: relative; }
  .features li::before {
    content: ""; position: absolute; left: -7px; top: 5px;
    width: 12px; height: 12px; border-radius: 50%;
    background: var(--leaf); z-index: -1;
  }
  .features--expect { left: 42px; top: 473px; width: 190px; }
  .features--offer { left: 263px; top: 535px; width: 310px; }
  .tagline {
    position: absolute; left: 43px; top: 764px;
    font-family: "Josefin Sans", sans-serif;
    font-size: 28px; font-weight: 400; color: var(--ink);
    white-space: nowrap;
  }
</style>
</head>
<body>
<main class="flyer">
  <section class="panel panel--cover">
    <svg class="photo" viewBox="0 0 587 830" role="img" aria-label="Foto: Holzfassade des Baumhauses mit Ziegeldach, Fenster, Terrasse mit Strandkorb, Tisch, Stühlen und Geländer">
      <defs>
        <linearGradient id="cover-photo" x1="0" y1="0" x2="0.25" y2="1">
          <stop offset="0" stop-color="var(--roof)"/>
          <stop offset="0.2" stop-color="#5a4a3e"/>
          <stop offset="0.28" stop-color="var(--wood-light)"/>
          <stop offset="0.58" stop-color="var(--wood-mid)"/>
          <stop offset="0.72" stop-color="var(--rail)"/>
          <stop offset="0.86" stop-color="#c4925e"/>
          <stop offset="1" stop-color="var(--grass)"/>
        </linearGradient>
      </defs>
      <polygon points="0,0 146,0 587,800 587,830 0,830" fill="url(#cover-photo)"/>
    </svg>
    <p class="brand">waldnest-kojen.de</p>
  </section>

  <section class="panel panel--info">
    <svg class="photo" viewBox="0 0 590 830" role="img" aria-label="Foto: heller Innenraum mit Bett, beleuchteter Holzdecke, Leiter, Essbereich und Schiebetür zum Bad">
      <defs>
        <linearGradient id="room-photo" x1="0" y1="0" x2="0.15" y2="1">
          <stop offset="0" stop-color="var(--ceiling)"/>
          <stop offset="0.28" stop-color="var(--ceiling-wood)"/>
          <stop offset="0.45" stop-color="var(--wall)"/>
          <stop offset="0.72" stop-color="#7a5e48"/>
          <stop offset="1" stop-color="var(--linen)"/>
        </linearGradient>
      </defs>
      <polygon points="0,0 590,0 590,330 0,461" fill="url(#room-photo)"/>
    </svg>
    <p class="brand">waldnest-kojen.de</p>

    <div class="features features--expect">
      <h2>Was Sie hier erwartet:</h2>
      <ul>
        <li>Ein barrierefreies Kiebitz-Baumhaus</li>
        <li>30qm in 4 Metern Höhe</li>
        <li>10 qm Außenterrasse</li>
        <li>Innenbreich: Bad, Pantry-Küche, Schlafbereich, Couchecke und Essbereich</li>
      </ul>
    </div>

    <div class="features features--offer">
      <h2>Wir bieten Ihnen:</h2>
      <ul>
        <li>Wlan, TV, Heizung, Kaminofen und eine voll ausgestattete Küche</li>
        <li>Haustierfreie und Haustierfreundliche Baumhäuser</li>
        <li>Bettwäsche, Handtücher und Kaminholz inklusive</li>
        <li>Tierbeobachtung möglich</li>
      </ul>
    </div>

    <p class="tagline">Ein wundervolles Erlebnis für 4 Personen</p>
  </section>
</main>
</body>
</html>
```